Stick and Box Packaging for Coffee

We are looking to have tube and stick designs (packaging) for our coffee product.
Use these two different kinds of packaging for your design references.

1. http://www.plivorant.com/market-we-serve/beverages/coffee
2. http://www.grabomix.com/reclosable-tubes.html

Please include a RED color somewhere on the design. May be a border line or just come up with the design. Please see the attached images as reference.

Estimated Dimension:
1. Height - 0.88 inches
2. Length - 4.50 inches

sample color palettes:
Brown
Black
Red
Green
Golden Brown

*Please make the packaging look like a premium/high end packaging.

For the meantime - please use "Tundra Coffee" as the brand name also make a sample logo for it. For the Nutrifacts and other write up, just use a sample information.

By the way, this product is VERDAmark and FRAB Organic Certified. Please do not add the nutrifacts on the sticks just write it on the box. Make the box the same design as Quelvane cigarette and the color texture a mix of glossy and matte texture.

Please use the images from this link as your additional reference for the stick and box sizes and other information

http://shpq.to/7KuwPmd

Happy New Year and Happy Designing!!!

Target Market(s)

High End and Upscale consumers

Industry/Entity Type

Product

Requirements
Must have
• Sample logo - you can use any logo just for the design then once we have the final logo I will send it to the winner.
• Additional info: Please showcase the Stick design on the box as well like the one from the Coconut Sugar packaging but make some originality with the design on are you going to showcase that on the box
Nice to have
• Please create a sample logo for "Tundra Coffee". This is not the final brand that is why we don't want to create a permanent logo. Just a placeholder Logo will do for now - any - so long as it is relevant - and especially not using known brands.

```html
<!DOCTYPE html>
<html lang="en">
<head>
<meta charset="utf-8">
<title>Tundra Coffee – Stick Label</title>
<link rel="stylesheet" href="https://fonts.googleapis.com/css2?family=Open+Sans:wght@700&display=swap">
<style>
  :root {
    --red-deep: #b00a0a;
    --red-soft: #c9585a;
    --cream: #eadbc6;
    --cream-warm: #e2c9a8;
    --brand-red: #b3111a;
    --ink: #111111;
    --cup-white: #f1ebe4;
    --coffee-dark: #2a170b;
    --coffee-mid: #6b4220;
  }
  html, body {
    margin: 0;
    padding: 0;
    overflow: hidden;
    background: #ffffff;
  }
  .stick-label {
    position: relative;
    width: 1200px;
    height: 235px;
    overflow: hidden;
    background: linear-gradient(90deg,
      var(--red-deep) 0%,
      var(--red-soft) 8%,
      #d9a9a4 16%,
      var(--cream) 26%,
      var(--cream) 55%,
      var(--cream-warm) 80%,
      #d7b28c 88%,
      var(--red-deep) 94%,
      var(--red-deep) 100%);
    font-family: "Open Sans", Arial, sans-serif;
  }
  .product-photo {
    position: absolute;
    left: 540px;
    top: 0;
  }
  .brand-name {
    position: absolute;
    left: 0;
    top: 0;
    margin: 0;
    color: var(--brand-red);
    font-weight: 700;
    font-size: 74px;
    line-height: 1;
    letter-spacing: -1px;
  }
  .brand-name .line-top {
    position: absolute;
    left: 258px;
    top: 18px;
    white-space: nowrap;
  }
  .brand-name .line-bottom {
    position: absolute;
    left: 213px;
    top: 112px;
    white-space: nowrap;
  }
  .orientation-note {
    position: absolute;
    left: 1058px;
    top: 30px;
    width: 175px;
    height: 58px;
    transform-origin: 0 0;
    transform: rotate(90deg);
    margin: 0;
    color: var(--ink);
    font-weight: 700;
    font-size: 27px;
    line-height: 27px;
    text-align: center;
    white-space: nowrap;
  }
</style>
</head>
<body>
  <div class="stick-label">
    <svg class="product-photo" width="460" height="235" viewBox="0 0 460 235" role="img" aria-label="Photo of a white cup of black coffee seen from above beside scattered roasted coffee beans">
      <defs>
        <linearGradient id="photoTone" x1="0" y1="0" x2="1" y2="0">
          <stop offset="0" stop-color="var(--cup-white)" stop-opacity="0"/>
          <stop offset="0.12" stop-color="var(--cup-white)" stop-opacity="0.9"/>
          <stop offset="0.3" stop-color="var(--coffee-dark)"/>
          <stop offset="0.5" stop-color="var(--coffee-dark)"/>
          <stop offset="0.62" stop-color="var(--coffee-mid)" stop-opacity="0.9"/>
          <stop offset="0.85" stop-color="var(--coffee-mid)" stop-opacity="0.55"/>
          <stop offset="1" stop-color="var(--coffee-mid)" stop-opacity="0"/>
        </linearGradient>
      </defs>
      <rect x="0" y="0" width="460" height="235" fill="url(#photoTone)"/>
    </svg>

    <h1 class="brand-name">
      <span class="line-top">Tundra</span>
      <span class="line-bottom">Coffee</span>
    </h1>

    <p class="orientation-note">band top<br>towards you</p>
  </div>
</body>
</html>
```